Professional business cards for real estate development company

I need business cards for my new real estate development company. The company, "KORVA" is a real estate development, investment, and advisory firm with a focus on multifamily, office, and mixed-use projects across primary and secondary markets in the Southeast United States.

Style preference is modern

Industry/Entity Type

Real Estate Development

Contact Information for Business Card

The business cards need to include:
Name
Title
Mailing Address
Phone Number
Web Address

Logo is attached. I would like white to be the primary color with incorporation of the company colors: #232D3A and #B5A451

Font styles to use
Other font styles liked:
• Montserrat, Avenir

Requirements
Must have
• Company Logo. No need to include the company name since the name is in the logo.
Should not have
• No line type designs

```html
<!DOCTYPE html>
<html lang="en">
<head>
<meta charset="utf-8">
<title>KORVA Business Cards</title>
<link href="https://fonts.googleapis.com/css2?family=Montserrat:wght@500;700&family=Mulish:wght@300;400&display=swap" rel="stylesheet">
<style>
  :root {
    --ink: #232d3a;
    --ink-soft: #6b6f75;
    --paper: #ffffff;
    --backdrop: #3a3a3c;
  }
  html, body {
    margin: 0;
    padding: 0;
    width: 1200px;
    height: 976px;
    overflow: hidden;
    background: var(--backdrop);
  }
  .sheet {
    position: relative;
    width: 1200px;
    height: 976px;
  }
  .card {
    position: absolute;
    left: 220px;
    width: 760px;
    height: 434px;
    background: var(--paper);
    box-shadow: 0 8px 24px rgba(0,0,0,0.35);
  }
  .card--front { top: 34px; }
  .card--back  { top: 508px; }

  /* Front */
  .wordmark {
    position: absolute;
    left: 0;
    right: 0;
    top: 160px;
    display: flex;
    justify-content: center;
    align-items: center;
    gap: 18px;
    font-family: "Montserrat", sans-serif;
    font-weight: 500;
    font-size: 64px;
    letter-spacing: 10px;
    color: var(--ink);
  }
  .wordmark__square {
    width: 22px;
    height: 22px;
    background: var(--ink);
  }
  .front-url {
    position: absolute;
    left: 0;
    right: 0;
    top: 330px;
    text-align: center;
    font-family: "Mulish", sans-serif;
    font-weight: 400;
    font-size: 17px;
    color: var(--ink-soft);
  }
  .front-url strong { color: var(--ink); font-weight: 400; }

  /* Back */
  .contact {
    position: absolute;
    left: 82px;
    top: 150px;
    font-family: "Mulish", sans-serif;
    color: var(--ink-soft);
  }
  .contact__name {
    margin: 0;
    font-family: "Montserrat", sans-serif;
    font-weight: 700;
    font-size: 30px;
    letter-spacing: 0.5px;
    color: var(--ink);
  }
  .contact__title {
    margin: 2px 0 18px;
    font-weight: 300;
    font-size: 20px;
  }
  .contact__address {
    margin: 0 0 14px 34px;
    font-style: normal;
    font-weight: 300;
    font-size: 20px;
    line-height: 1.25;
  }
  .contact__list {
    list-style: none;
    margin: 0;
    padding: 0;
    font-weight: 300;
    font-size: 20px;
    line-height: 1.5;
  }
  .contact__list li {
    display: flex;
    align-items: center;
    gap: 10px;
  }
  .contact__icon {
    width: 18px;
    height: 18px;
    fill: var(--ink);
    flex: none;
  }
</style>
</head>
<body>
<main class="sheet">
  <section class="card card--front" aria-label="Card front">
    <div class="wordmark"><span class="wordmark__square"></span>KORVA</div>
    <p class="front-url">www.<strong>korva</strong>.com</p>
  </section>

  <section class="card card--back" aria-label="Card back">
    <div class="contact">
      <h1 class="contact__name">DANA WHITFIELD</h1>
      <p class="contact__title">President</p>
      <address class="contact__address">48 Alder Ridge Parkway<br>Suite 310, GA 30305</address>
      <ul class="contact__list">
        <li>
          <svg class="contact__icon" viewBox="0 0 24 24" aria-hidden="true"><path d="M6.6 10.8a15.5 15.5 0 0 0 6.6 6.6l2.2-2.2a1 1 0 0 1 1-.25 11.4 11.4 0 0 0 3.6.57 1 1 0 0 1 1 1V20a1 1 0 0 1-1 1A17 17 0 0 1 3 4a1 1 0 0 1 1-1h3.5a1 1 0 0 1 1 1c0 1.25.2 2.45.57 3.6a1 1 0 0 1-.25 1z"/></svg>
          404 555 0182
        </li>
        <li>
          <svg class="contact__icon" viewBox="0 0 24 24" aria-hidden="true"><path d="M2 5h20v14H2z M4 7v.5l8 5.5 8-5.5V7z" fill-rule="evenodd"/></svg>
          info@korva.com
        </li>
        <li>
          <svg class="contact__icon" viewBox="0 0 24 24" aria-hidden="true"><circle cx="12" cy="12" r="10"/><path d="M2 12h20M12 2c3 3 3 17 0 20M12 2c-3 3-3 17 0 20M4 7h16M4 17h16" stroke="#fff" stroke-width="1.2" fill="none"/></svg>
          www.korva.com
        </li>
      </ul>
    </div>
  </section>
</main>
</body>
</html>
```